Stand bag for exclusive, natural snacks

We are looking for a PP stand bag design that will be used to pack exclusive snacks (dried fruits). These snacks will be 100% natural, healthy and without any chemicals. For that reason and for the fact that these products will have a higher price point, the stand bag design should look very premium and happy, while still reminding the customer of the natural, healthy benefits of the snacks inside. The main colors of our brand are black and gold, so we would like to see the packaging in similar colors. In order to be able to see the product, we usually leave some part of the PP packaging transparent.
Packaging Size: h170mm x w80mm x d30mm

Target Market(s)

High-end retail markets with consumers that are willing to pay a little more to get a high-quality product, free from any preservatives and completely natural.

Font styles to use
Sans Serif

Colors

Designer to choose colors to be used in the design.

Requirements
Must have
• - similar to the bag in the sample photos
• - bag size: h170mm x w80mm x d30mm
• - Our logo
• - the colors black & gold
• - Some way of showing the customer the benefit of our dried fruits (healthy, natural, happy)
• - a transparent part to see the product through the plastic foil
Nice to have
• - bottom maybe not transparent in order not to see dust that falls to the bottom

```html
<!DOCTYPE html>
<html lang="en">
<head>
<meta charset="utf-8">
<title>Aurel Pantry – Stand Bags</title>
<link rel="stylesheet" href="https://fonts.googleapis.com/css2?family=Josefin+Sans:wght@400;600&display=swap">
<style>
  :root {
    --bg: #ffffff;
    --bag: #0e1422;
    --bag-edge: #1b2335;
    --seal-line: #2a3449;
    --gold: #c9a85a;
    --ink: #1a1a1a;
    --mango: #f7941d;
    --kiwi: #8cc63f;
  }
  * { margin: 0; padding: 0; box-sizing: border-box; }
  html, body { width: 1200px; height: 983px; overflow: hidden; background: var(--bg); }
  body { position: relative; font-family: "Josefin Sans", sans-serif; }

  .bag {
    position: absolute;
    top: 38px;
    width: 457px;
    height: 909px;
    background: linear-gradient(90deg, var(--bag-edge) 0%, var(--bag) 12%, var(--bag) 88%, var(--bag-edge) 100%);
    border-radius: 10px;
  }
  .bag--mango { left: 102px; }
  .bag--kiwi  { left: 658px; }

  .bag__seal {
    position: absolute;
    left: 0; right: 0;
    height: 2px;
    background: var(--seal-line);
  }
  .bag__seal--1 { top: 62px; }
  .bag__seal--2 { top: 92px; }
  .bag__seal--3 { top: 128px; }

  .bag__tagline {
    position: absolute;
    top: 276px; left: 0; right: 0;
    text-align: center;
    color: var(--gold);
    font-size: 17px;
    letter-spacing: 0.5px;
  }

  .bag__brand {
    position: absolute;
    top: 345px; left: 0; right: 0;
    text-align: center;
    color: var(--gold);
    font-size: 40px;
    font-weight: 600;
    letter-spacing: 2px;
  }

  .bag__window {
    position: absolute;
    top: 445px; left: 57px;
    width: 356px; height: 295px;
    border-radius: 16px;
  }
  .bag--mango .bag__window { background: linear-gradient(160deg, #f0a24a 0%, #c4672a 45%, #e8b36a 100%); }
  .bag--kiwi  .bag__window { background: linear-gradient(160deg, #c8dc6a 0%, #9cc23c 50%, #d3e38a 100%); }

  .bag__label {
    position: absolute;
    top: 762px; left: 89px;
    width: 248px; height: 40px;
    border-radius: 12px;
    display: flex; align-items: center; justify-content: center;
    color: var(--ink);
    font-size: 21px;
    font-weight: 600;
    text-transform: uppercase;
    padding-top: 3px;
  }
  .bag--mango .bag__label { background: var(--mango); }
  .bag--kiwi  .bag__label { background: var(--kiwi); }
</style>
</head>
<body>
  <section class="bag bag--mango">
    <div class="bag__seal bag__seal--1"></div>
    <div class="bag__seal bag__seal--2"></div>
    <div class="bag__seal bag__seal--3"></div>
    <p class="bag__tagline">DRIED NATURAL FRUITS</p>
    <p class="bag__brand">Aurel Pantry</p>
    <div class="bag__window" role="img" aria-label="Transparent window showing dried mango and mixed dried fruit pieces"></div>
    <p class="bag__label">Dried Mango</p>
  </section>

  <section class="bag bag--kiwi">
    <div class="bag__seal bag__seal--1"></div>
    <div class="bag__seal bag__seal--2"></div>
    <div class="bag__seal bag__seal--3"></div>
    <p class="bag__tagline">DRIED NATURAL FRUITS</p>
    <p class="bag__brand">Aurel Pantry</p>
    <div class="bag__window" role="img" aria-label="Transparent window showing sugared dried kiwi slices"></div>
    <p class="bag__label">Dried Kiwi</p>
  </section>
</body>
</html>
```